Australian Careers Business Needs 2 Banner Ad Design

We need a banner ad design for a new company based in Australia called Bright Sparrows. We provide career tools and insights to young professionals. Our target market is 20-30 year olds.

We would like to see designs that attract users on the site to click on the banner and sign up for a weekly newsletter. The newsletter will feature a blog, cheat sheets etc. Inspiration in their inbox!

The second banner is to attract users to sign up for a Horizon Gathering. They would click on it to find out more information and then register with their email address. This convention is a 1 day workshop designed to enhance young professionals abilities to give their best at work. There will CEO insights etc.

Use of images or flash is ok. Needs to look very professional and presented in accordance to the current colour scheme in place. Visit http://www.brightsparrows-demo.com/home to understand.

Banner sizes 300 x 250.
Mandatory use of Corporate Colours required on Font.
R66 G73 B74
R242 G240 B230
R38 G128 B138

No logo necessary.

Hi All,As both banners will feature on the Bright Sparrows site there is no need for a logo or hyperlink to the site.I would like to see some better images, and a bit more creative flair.Please don't use single female images as I am wanting to avoid the women in business perception. We cater to young professionals.Some suggestions for lines to utilise on the newsletter ad:Click here for weekly career tipsInvest in your career for free hereJoin the weekly conversationWeekly career tips in your inboxSign up for our weekly newsletterSome suggestions for lines to use on the horizon gathering ad:Register for the Horizon Gathering - Find out how to get ahead of your peersAre you a millennial climbing the corporate ladder? Find out how to rise to the topInterested in hearing from experts who recognise millennials are our future business leaders? Click here.Thanks,Megan Added Friday, April 3, 2015

Target Market(s)

20-30 years

Industry/Entity Type

Business

Font styles to use
Sans Serif

Requirements
Must have
• Please use images in the attached as options
Should not have
• NO LOGO - Its already onsite so not needed.

```html
<!DOCTYPE html>
<html lang="en">
<head>
<meta charset="utf-8">
<title>Bright Sparrows Banners</title>
<link rel="stylesheet" href="https://fonts.googleapis.com/css2?family=Open+Sans:wght@400;600;700&family=Oswald:wght@600;700&family=PT+Sans+Narrow:wght@400;700&display=swap">
<style>
  :root {
    --page: #ffffff;
    --teal: #1f7b80;
    --navy: #07051f;
    --white: #ffffff;
    --button-light: #ecedee;
    --ink: #0a0a0a;
    --button-dark: #1a1a1a;
  }
  * { box-sizing: border-box; margin: 0; padding: 0; }
  html, body {
    width: 1200px; height: 1200px; overflow: hidden;
    background: var(--page);
  }
  .canvas { position: relative; width: 1200px; height: 1200px; }
  .banner {
    position: absolute; top: 389px;
    width: 300px; height: 250px; overflow: hidden;
    transform: scale(1.2); transform-origin: 0 0;
  }
  .banner--newsletter { left: 190px; }
  .banner--gathering { left: 592px; }

  /* Newsletter banner */
  .team-photo {
    position: absolute; inset: 0;
    background: linear-gradient(135deg, #f1f2f4 0%, #d9dde3 30%, #8a8f99 55%, #e7e8ec 80%, #b4a8c8 100%);
  }
  .teal-wedge { position: absolute; inset: 0; }
  .newsletter-title {
    position: absolute; right: 10px; top: 82px;
    font-family: "PT Sans Narrow", sans-serif; font-weight: 400;
    font-size: 22px; line-height: 23px; letter-spacing: 0.5px;
    color: var(--white); text-align: right; text-transform: uppercase;
  }
  .join-button {
    position: absolute; left: 208px; top: 145px;
    width: 81px; height: 28px; border-radius: 5px;
    background: var(--button-light);
    font-family: "Open Sans", sans-serif; font-weight: 700;
    font-size: 20px; line-height: 28px; color: var(--navy);
    text-align: center; letter-spacing: 0.5px;
  }
  .brand-bar {
    position: absolute; left: 0; bottom: 0; width: 276px; height: 28px;
    background: var(--navy);
  }
  .brand-bar__name {
    position: absolute; left: 0; width: 276px; bottom: 0; height: 28px;
    font-family: "Open Sans", sans-serif; font-weight: 600;
    font-size: 15.5px; line-height: 28px; color: var(--white);
    text-align: center; text-transform: uppercase;
  }

  /* Gathering banner */
  .speaker-photo {
    position: absolute; inset: 0;
    background:
      radial-gradient(circle at 88% 72%, #e6fbf8 0%, #9fe3dc 12%, rgba(80,190,180,0) 40%),
      linear-gradient(100deg, #8d9193 0%, #b8bcbc 25%, #7cc9c2 60%, #3dbdb0 100%);
  }
  .gathering-copy {
    position: absolute; left: 148px; top: 20px; width: 150px;
    color: var(--ink);
  }
  .gathering-brand {
    font-family: "Open Sans", sans-serif; font-weight: 600;
    font-size: 17px; line-height: 17px; letter-spacing: 2.4px;
    color: var(--white); text-transform: uppercase;
  }
  .gathering-lead, .gathering-tail {
    font-family: "Open Sans", sans-serif; font-weight: 400;
    font-size: 12.5px; line-height: 15px; letter-spacing: 1px;
  }
  .gathering-lead { margin-top: 28px; }
  .gathering-headline {
    font-family: "Oswald", sans-serif; font-weight: 700;
    text-transform: uppercase; letter-spacing: 1.5px; line-height: 1;
  }
  .gathering-headline--one { font-size: 20px; margin-top: 3px; }
  .gathering-headline--two { font-size: 25px; margin-top: 3px; }
  .gathering-tail { margin-top: 1px; }
  .click-button {
    position: absolute; left: 150px; top: 203px;
    width: 111px; height: 31px; border-radius: 16px;
    background: var(--button-dark); border: 1px solid #4a4a4a;
    font-family: "Open Sans", sans-serif; font-weight: 700;
    font-size: 12.5px; line-height: 29px; letter-spacing: 1px;
    color: var(--white); text-align: center; text-transform: uppercase;
  }
</style>
</head>
<body>
<main class="canvas">
  <section class="banner banner--newsletter">
    <div class="team-photo" role="img" aria-label="Photo of young professionals in business attire gathered around a whiteboard"></div>
    <svg class="teal-wedge" viewBox="0 0 300 250" width="300" height="250" aria-hidden="true">
      <polygon points="119,122 300,0 300,250" fill="var(--teal)"/>
    </svg>
    <h2 class="newsletter-title">The Weekly<br>Conversation</h2>
    <div class="join-button">JOIN</div>
    <div class="brand-bar"><span class="brand-bar__name">Bright Sparrows</span></div>
  </section>

  <section class="banner banner--gathering">
    <div class="speaker-photo" role="img" aria-label="Photo of a speaker on stage behind a lectern with microphones, arms raised under bright teal lights"></div>
    <div class="gathering-copy">
      <p class="gathering-brand">Bright<br>Sparrows</p>
      <p class="gathering-lead">Are you a</p>
      <p class="gathering-headline gathering-headline--one">Millennial</p>
      <p class="gathering-headline gathering-headline--two">Climbing</p>
      <p class="gathering-tail">the corporate<br>ladder?</p>
    </div>
    <div class="click-button">Click Here</div>
  </section>
</main>
</body>
</html>
```